Business Advisory Firm Business Card

A clean, very upscale looking business card. Not crowded.

Please include logo (attached) and:

Daria K. Pellworth
Four Marlow Court
New York, NY 10023
tel: (917) 555-0143
fax: (646) 555-0172
email: dpellworth@quarrystoneconsultants.example
website: www.quarrystoneconsultants.example

Target Market(s)

Business clients. Often real estate development firms, other advisory firms or growing companies that need assistance. I would like a card that looks impressive and confident.

Industry/Entity Type

Business

Colors

Designer to choose colors to be used in the design.

Requirements
Must have
• Impressive and confident. Please include logo.
Should not have
• nothing flashy...

```html
<!DOCTYPE html>
<html lang="en">
<head>
<meta charset="utf-8">
<title>Quarrystone Advisory Services – Business Card</title>
<link href="https://fonts.googleapis.com/css2?family=Exo+2:wght@400;500&display=swap" rel="stylesheet">
<style>
  :root {
    --page: #e8e8e6;
    --card: #ffffff;
    --green: #8cc63f;
    --green-light: #b2dc6a;
    --ink: #3a3a3a;
    --ink-soft: #6b6b6b;
    --icon: #555555;
    --mark: #8d8d8d;
  }
  * { margin: 0; padding: 0; box-sizing: border-box; }
  html, body {
    width: 1200px; height: 901px; overflow: hidden;
    background: var(--page);
    font-family: "Exo 2", Arial, sans-serif;
    color: var(--ink);
  }
  .card {
    position: absolute; left: 250px;
    width: 700px; height: 400px;
    background: var(--card);
    overflow: hidden;
    box-shadow: 0 6px 18px rgba(0,0,0,.12);
  }
  .card--front { top: 40px; }
  .card--back { top: 461px; }
  .card__edge {
    position: absolute; left: 0; right: 0; bottom: 0;
    height: 7px; background: var(--green);
  }
  .ribbons { position: absolute; inset: 0; }

  .brand { position: absolute; display: flex; align-items: center; gap: 22px; }
  .brand__square { width: 104px; height: 104px; background: var(--mark); flex: none; }
  .brand__name {
    font-weight: 500; font-size: 27px; line-height: 1.02;
    text-transform: uppercase; letter-spacing: .5px; color: var(--ink);
  }
  .card--front .brand { left: 175px; top: 130px; }
  .card--back .brand { left: 215px; top: 38px; }
  .card--back .brand__square { width: 80px; height: 80px; }
  .card--back .brand__name { font-size: 22px; }

  .person { position: absolute; left: 48px; top: 172px; }
  .person__name { font-size: 19px; font-weight: 500; letter-spacing: 1px; text-transform: uppercase; color: var(--ink-soft); }
  .person__title { font-size: 11px; letter-spacing: 1px; text-transform: uppercase; color: var(--ink); margin-top: 2px; }

  .contact { position: absolute; list-style: none; }
  .contact li { display: flex; align-items: center; gap: 12px; font-size: 13px; line-height: 1.3; margin-bottom: 8px; color: var(--ink); }
  .contact li:last-child { margin-bottom: 0; }
  .contact--personal { left: 48px; top: 228px; }
  .contact--online { left: 390px; top: 178px; }
  .contact--online li { margin-bottom: 14px; }
  .icon {
    width: 24px; height: 24px; background: var(--icon); border-radius: 3px;
    display: flex; align-items: center; justify-content: center; flex: none;
  }
  .icon svg { width: 14px; height: 14px; }
</style>
</head>
<body>

<section class="card card--front">
  <svg class="ribbons" viewBox="0 0 700 400" aria-hidden="true">
    <polygon points="0,150 0,104 150,22 205,30 172,50 186,72 36,150" fill="var(--green)"/>
    <polygon points="0,150 36,150 186,72 172,50" fill="var(--green-light)" opacity=".55"/>
    <polygon points="455,0 535,0 700,95 700,138" fill="var(--green)"/>
    <polygon points="495,0 535,0 700,95 700,115" fill="var(--green-light)" opacity=".55"/>
  </svg>
  <div class="brand">
    <span class="brand__square"></span>
    <p class="brand__name">Quarrystone<br>Advisory<br>Services, Inc.</p>
  </div>
  <span class="card__edge"></span>
</section>

<section class="card card--back">
  <div class="brand">
    <span class="brand__square"></span>
    <p class="brand__name">Quarrystone<br>Advisory<br>Services, Inc.</p>
  </div>

  <div class="person">
    <p class="person__name">Daria K. Pellworth</p>
    <p class="person__title">Financial Advisor</p>
  </div>

  <ul class="contact contact--personal">
    <li><span class="icon"><svg viewBox="0 0 14 14"><path d="M7 1a4 4 0 0 0-4 4c0 3 4 8 4 8s4-5 4-8a4 4 0 0 0-4-4zm0 5.5A1.5 1.5 0 1 1 7 3.5a1.5 1.5 0 0 1 0 3z" fill="#fff"/></svg></span><span>Four Marlow Court<br>New York, NY 10023</span></li>
    <li><span class="icon"><svg viewBox="0 0 14 14"><path d="M4 1.5l2 2.5-1.2 1.5a7 7 0 0 0 3.7 3.7L10 8l2.5 2-1 2.2C6 12 2 8 1.8 2.5z" fill="#fff"/></svg></span>tel: (917) 555-0143</li>
    <li><span class="icon"><svg viewBox="0 0 14 14"><rect x="3.5" y="1.5" width="7" height="4" fill="#fff"/><rect x="1.5" y="6" width="11" height="5" rx="1" fill="#fff"/><rect x="3.5" y="9.5" width="7" height="3" fill="#fff" stroke="var(--icon)" stroke-width=".8"/></svg></span>fax: (646) 555-0172</li>
    <li><span class="icon"><svg viewBox="0 0 14 14"><rect x="1.5" y="3" width="11" height="8" fill="#fff"/><path d="M1.5 3L7 7.5 12.5 3" stroke="var(--icon)" stroke-width="1.2" fill="none"/></svg></span>dpellworth@quarrystoneconsultants.example</li>
  </ul>

  <ul class="contact contact--online">
    <li><span class="icon"><svg viewBox="0 0 14 14"><g stroke="#fff" stroke-width="1.1" fill="none"><circle cx="7" cy="7" r="5.5"/><ellipse cx="7" cy="7" rx="2.3" ry="5.5"/><path d="M1.5 7h11"/></g></svg></span>www.quarrystoneconsultants.example</li>
    <li><span class="icon"></span>www.chirpline.example</li>
    <li><span class="icon"></span>www.friendsheet.example</li>
  </ul>

  <span class="card__edge"></span>
</section>

</body>
</html>
```